Soltravex business card

a nice business card with the logo,
Soltravex
Delia Vostrand
Marketing Director
CH-1296 Geneva
Switzerland
+41 79 612 3048
email: Delia.Vostrand@soltravex-mail.net

Target Market(s)

fertilizer business people, very nice and classic business card, normal size, make it nice and funky, try to make it different from the normal boring ones if possible.

Industry/Entity Type

Farming

Number of Pages Required

1 page

Requirements
Must have
• logo, Soltravex, my name - mail and phone number
regular business card size for me to print easy please

```html
<!DOCTYPE html>
<html lang="en">
<head>
<meta charset="utf-8">
<title>Soltravex business card</title>
<link rel="stylesheet" href="https://fonts.googleapis.com/css2?family=Carlito:wght@400;700&display=swap">
<style>
  :root {
    --page: #ffffff;
    --lime: #a4ff0a;
    --lime-text: #a6f00a;
    --stone: #939e9b;
    --edge: #333333;
    --white: #ffffff;
  }
  * { margin: 0; padding: 0; box-sizing: border-box; }
  html, body {
    width: 1200px;
    height: 1200px;
    overflow: hidden;
    background: var(--page);
    font-family: "Carlito", "Calibri", sans-serif;
  }
  .sheet { position: relative; width: 1200px; height: 1200px; }

  .card {
    position: absolute;
    left: 250px;
    width: 700px;
    height: 400px;
  }
  .card-front { top: 145px; border: 1px solid var(--edge); background: var(--white); }
  .card-back { top: 655px; background: var(--lime); }

  .brand-block {
    position: absolute;
    left: 0;
    top: 0;
    width: 257px;
    height: 100%;
  }
  .brand-dot {
    position: absolute;
    left: 90px;
    top: 130px;
    width: 66px;
    height: 66px;
    border-radius: 50%;
    background: var(--lime);
  }
  .brand-name {
    position: absolute;
    left: 48px;
    top: 293px;
    font-size: 16px;
    font-weight: 700;
    letter-spacing: 8.6px;
    color: var(--stone);
    text-transform: uppercase;
    white-space: nowrap;
  }

  .divider {
    position: absolute;
    left: 256px;
    top: 58px;
    width: 3px;
    height: 284px;
    background: var(--stone);
  }

  .contact {
    position: absolute;
    left: 302px;
    top: 46px;
    font-size: 22px;
    line-height: 30px;
    color: var(--stone);
    white-space: nowrap;
  }
  .contact p { margin: 0; }
  .contact .person { color: var(--lime-text); font-weight: 700; text-transform: uppercase; }
  .contact .company { font-weight: 700; text-transform: uppercase; margin-top: 30px; }

  .back-name {
    position: absolute;
    left: 202px;
    top: 330px;
    font-size: 30px;
    font-weight: 700;
    letter-spacing: 14.5px;
    color: var(--white);
    text-transform: uppercase;
    white-space: nowrap;
  }
</style>
</head>
<body>
  <div class="sheet">
    <section class="card card-front">
      <div class="brand-block">
        <span class="brand-dot"></span>
        <span class="brand-name">Soltravex</span>
      </div>
      <span class="divider"></span>
      <div class="contact">
        <p class="person">Delia Vostrand</p>
        <p class="role">Marketing Director</p>
        <p class="company">Soltravex</p>
        <p>CH-1296 Geneva</p>
        <p>Switzerland</p>
        <p>+41 79 612 3048</p>
        <p>delia.vostrand@soltravex-mail.net</p>
      </div>
    </section>

    <section class="card card-back">
      <span class="back-name">Soltravex</span>
    </section>
  </div>
</body>
</html>
```